Commercial Construction Company

We need a business card design based on our current logo. We are a commercial general contractor based in Southern California that specializes in bank remodels. We would like to see designs that incorporate dark blue. The final design should portray an image of professionalism and quality.

If possible, I would like to add metallic foil to the design. Thank you

```html
<!DOCTYPE html>
<html lang="en">
<head>
<meta charset="utf-8">
<title>Halvorsen Commercial – Business Card</title>
<link href="https://fonts.googleapis.com/css2?family=Open+Sans:wght@400;600;700&display=swap" rel="stylesheet">
<style>
  :root {
    --stage: #d9dadc;
    --navy: #0d4476;
    --navy-text: #0f4a85;
    --ink: #1c1c1c;
    --card-white: #f4f4f4;
    --divider: #9a9a9a;
    --foil: #c9ccd1;
    --logo-grey: #8e8e8e;
  }
  * { margin: 0; padding: 0; box-sizing: border-box; }
  html, body {
    width: 1200px; height: 1021px; overflow: hidden;
    background: var(--stage);
    font-family: "Open Sans", Arial, sans-serif;
  }
  .card {
    position: absolute; left: 250px;
    width: 700px; height: 400px;
    box-shadow: 0 6px 18px rgba(0,0,0,.18);
  }
  /* Back of card */
  .card-back { top: 70px; background: var(--navy); display: flex; align-items: center; justify-content: center; }
  .brand { display: flex; align-items: center; gap: 16px; }
  .brand-dot { width: 34px; height: 34px; border-radius: 50%; }
  .card-back .brand-dot { background: var(--foil); }
  .card-back .brand-name { color: var(--foil); font-weight: 700; font-size: 34px; letter-spacing: .5px; }

  /* Front of card */
  .card-front { top: 550px; background: var(--card-white); }
  .front-brand { position: absolute; left: 40px; top: 110px; width: 300px; }
  .front-brand .brand-dot { background: var(--logo-grey); width: 28px; height: 28px; }
  .front-brand .brand-name { color: var(--ink); font-weight: 700; font-size: 25px; line-height: 1.15; }
  .divider { position: absolute; left: 366px; top: 60px; width: 1px; height: 220px; background: var(--divider); }
  .contact { position: absolute; left: 396px; top: 62px; }
  .person-name { color: var(--navy-text); font-weight: 700; font-size: 22px; line-height: 1.1; }
  .person-role { color: var(--ink); font-size: 17px; margin-bottom: 8px; }
  .contact-list { list-style: none; font-size: 16.5px; color: var(--ink); line-height: 1.32; }
  .contact-list li { display: flex; align-items: center; gap: 8px; }
  .contact-list svg { width: 15px; height: 15px; fill: var(--navy-text); flex: none; }
  .contact-list .web { color: var(--navy-text); }
  .contact-list .license { margin-left: -4px; }
  .address { position: absolute; left: 40px; top: 330px; font-size: 17px; color: var(--ink); }
</style>
</head>
<body>

<section class="card card-back" aria-label="Card back">
  <div class="brand">
    <span class="brand-dot"></span>
    <span class="brand-name">Halvorsen Commercial</span>
  </div>
</section>

<section class="card card-front" aria-label="Card front">
  <div class="front-brand brand">
    <span class="brand-dot"></span>
    <span class="brand-name">Halvorsen<br>Commercial</span>
  </div>

  <div class="divider"></div>

  <div class="contact">
    <p class="person-name">Daniel Mercer</p>
    <p class="person-role">Founder &amp; Owner</p>
    <ul class="contact-list">
      <li><svg viewBox="0 0 24 24"><path d="M6.6 10.8a15 15 0 0 0 6.6 6.6l2.2-2.2a1 1 0 0 1 1-.25 11.4 11.4 0 0 0 3.6.57 1 1 0 0 1 1 1V20a1 1 0 0 1-1 1A17 17 0 0 1 3 4a1 1 0 0 1 1-1h3.5a1 1 0 0 1 1 1c0 1.25.2 2.45.57 3.57a1 1 0 0 1-.25 1z"/></svg>(555) 214-0386</li>
      <li><svg viewBox="0 0 24 24"><path d="M6.6 10.8a15 15 0 0 0 6.6 6.6l2.2-2.2a1 1 0 0 1 1-.25 11.4 11.4 0 0 0 3.6.57 1 1 0 0 1 1 1V20a1 1 0 0 1-1 1A17 17 0 0 1 3 4a1 1 0 0 1 1-1h3.5a1 1 0 0 1 1 1c0 1.25.2 2.45.57 3.57a1 1 0 0 1-.25 1z"/></svg>(800) 555-0142 Toll Free</li>
      <li><svg viewBox="0 0 24 24"><path d="M6 2h12v6H6zM3 9h18a1 1 0 0 1 1 1v8h-4v4H6v-4H2v-8a1 1 0 0 1 1-1zm5 8v3h8v-3z"/></svg>(555) 214-0391</li>
      <li><svg viewBox="0 0 24 24"><path d="M2 5h20v14H2zm2 2v.5l8 5.5 8-5.5V7zm0 3v7h16v-7l-8 5.5z"/></svg>daniel@halvorsenbuild.com</li>
      <li class="web"><svg viewBox="0 0 24 24"><path d="M12 2a10 10 0 1 0 0 20 10 10 0 0 0 0-20zm7.9 9h-3.4a15 15 0 0 0-1.4-6 8 8 0 0 1 4.8 6zM12 4.1c.9 1.2 2.2 3.6 2.5 6.9h-5c.3-3.3 1.6-5.7 2.5-6.9zM8.9 5a15 15 0 0 0-1.4 6H4.1a8 8 0 0 1 4.8-6zM4.1 13h3.4a15 15 0 0 0 1.4 6 8 8 0 0 1-4.8-6zm7.9 6.9c-.9-1.2-2.2-3.6-2.5-6.9h5c-.3 3.3-1.6 5.7-2.5 6.9zm3.1-.9a15 15 0 0 0 1.4-6h3.4a8 8 0 0 1-4.8 6z"/></svg>www.halvorsenbuild.com</li>
      <li class="license">Contractor's License #480215</li>
    </ul>
  </div>

  <p class="address">2150 Juniper Ridge Road, Suite 410, Ontario Hills, CA 91800</p>
</section>

</body>
</html>
```